A landing page for a market leader in France

Our start-up represents a network of professional trainers both independent and working for training organizations. Above all our mission consists of managing administrative and legal procedures necessary to become a training organization. Secondly, our job envisages the obtaining of public financing (subsidies) for customers of our members who wish to receive professional training by fully dealing with the necessary administrative steps. We are providing you with a full presentation of our market, company, services and our particular expectations from the landing page. Briefly: http://www.velmora-exemple.fr/pro/home https://www.velmora-exemple.fr/pro/tariffs membership https: //www.velmora-exemple. fr / pro / rates-management The landing page must contain the following elements: Presentation of the VLMRA and our added value. What do we expect from our landing page? We have a new page of our landing page to a one-page web site with many sections to present the added value of our service, the pricing and the differences between our types of subscription. The landing page has been condensed to a more generalized version of our web-site but clearer, with fewer fields, more information, and more. It also requires reinsurance with customer reviews or cases: https://www.videohub-exemple.com/channel/UCxQwErTy7uIoPaSdFgHjKLZ/videos Graphic design - we prefer to keep your current charter. Please find attached our logo as we are different graphic elements (the main color code: RGB: 08133B). The landing page must be available in a mobile version. Our services 1. Membership To join VLMRA To join the VLMRA you have to pay a membership that is valid for life. The amount of membership varies depending on whether or not it is one of several. Depending on your membership VLMRA can manage all the administrative procedures needed to launch your activity - a so-called "activity declaration". The membership includes activity launching support, pedagogical support, one or more training courses of the trainer, as well as licenses to use our management software. Membership can be paid in 1 to 12 installments (the shorter the payment, the lower the fee). Membership can be paid in 1 to 12 installments (the quicker payment, the lower the fee). The membership is explained on our web-site (eventually, the designer will compete for your current site: https://www.velmora-exemple.fr/pro/tarifs-adhesion) 2. Each VLMRA member who benefits from the management of their trainees. We offer 4 options to manage the training and the possible funding: A. The member wants to manage the funding himself: he uses a documentary pack provided. The documents are in accordance with the expectations of financing mechanisms. This option is free and unlimited but does not consider any support. It's autonomous management. B. The member wants to make the compsory documents but it will not be the subject of public subsidy (30 to 50 €). This management is called "Secretariat." C. The member wants to get a handle on the subject of customer satisfaction. This is "Financial managment" D. The member wants to manage the process and optimize the funding: we fully manage the administrative and financial This method is the flagship and premium service of VLMRA that makes it possible for us to finance the customer. subsidies), the cost is equal to 10 and 25% of the amount of the fee. If he does not buy the subscription, the fees will be the highest, while he pays for subscription, it will reduce the fees and give an access to complementary services. We offer 3 types of subscription: Free: includes estimates of service for customers of different types of membership, different modes of management listed above, and a complementary cost method. Partner: all the "Free" subscription features with reduced fees, priority matching, unlimited programs validation, possibility to obtain subsidies the possibility of obtaining within the DLT and for job seekers. Partner: all the "Partner" subscription features with dedicated support and reduced management fees. This pricing you will find on our web-site: https://www.velmora-exemple.fr/pro/tariffs-management
Target Market(s)
Therefore, most of our customers are future professionals who wish to launch their training activities. But we also target companies that offer a service and want to provide customers with this service (eg I sell Pagelark services and want to learn my customers to use it).
Number of Pages Required
1 page
Requirements
Must have
- We need to popularize the complexity of the market and make it clear that it's much easier with us!
Nice to have
- Main color theme: RGB: 08133B

```html
<!DOCTYPE html>
<html lang="fr">
<head>
<meta charset="utf-8">
<title>VLMRA — Vous formez vos clients</title>
<link href="https://fonts.googleapis.com/css2?family=Lato:wght@400;700;900&display=swap" rel="stylesheet">
<style>
  :root {
    --ink: #08133B;
    --paper: #ffffff;
  }
  html, body {
    margin: 0;
    width: 1200px;
    height: 1000px;
    overflow: hidden;
    background: var(--paper);
    color: var(--ink);
    font-family: "Lato", sans-serif;
  }
  .feature {
    position: absolute;
    left: 193px;
    width: 820px;
  }
  .feature--services { top: 232px; }
  .feature--software { top: 531px; }
  .feature__title {
    margin: 0;
    font-weight: 900;
    font-size: 50px;
    line-height: 64px;
    letter-spacing: -0.5px;
  }
  .feature__text {
    margin: 38px 0 0;
    font-size: 19px;
    line-height: 24px;
    font-weight: 400;
  }
</style>
</head>
<body>
  <section class="feature feature--services">
    <h2 class="feature__title">Vous formez vos clients, on s’occupe du reste!</h2>
    <p class="feature__text">Nous avons décidé de tout faire pour vous ! Secrétariat, recherche et optimisation de financement, traitement de vos obligations annuelles...</p>
  </section>
  <section class="feature feature--software">
    <h2 class="feature__title">Logiciel de gestion offert à tous<br>nos adhérents</h2>
    <p class="feature__text">Dès lors que vous rejoignez le VLMRA, vous bénéficiez d’un logiciel complet. Suivi de vos dossiers, gestion du e-learning, édition de document, tout ce dont vous avez besoin est compris.</p>
  </section>
</body>
</html>
```